Create print ready logo with business card and stationery

I have a logo created in Photoshop, but I need it vectorized properly so it can be used for print, outdoor signs etc. The logo should be able to scale between 2 cm and at least 3 meters in width. And to be printed using standard printing methods.

I would also want to have your help in creating business cards and stationery. The company is a school so the design for cards and stationery should be simple and NOT be "cute" just because it is a school. Use the logo and colors provided. I would want originals which I could edit names, positions, phone etc in.

I would want originals in jpg, png, eps, ai, psd and pdf with correct color codes (CMYK, RGB etc) so it can be used for both print and on web. I would want ONE separate file per version of the logo. It's actually just two logos and variations of colors. I want the logos both with and without background boxes (black or white).

```html
<!DOCTYPE html>
<html lang="en">
<head>
<meta charset="utf-8">
<title>Solvik Grundskola – Business Card</title>
<link href="https://fonts.googleapis.com/css2?family=Josefin+Sans:wght@300;400&family=Open+Sans:wght@400;600&display=swap" rel="stylesheet">
<style>
  :root{
    --backdrop:#2b2b2d;
    --band:#4a4a4d;
    --band-dark:#3a3a3c;
    --paper:#f7f7f7;
    --accent:#d9262c;
    --ink:#4a4a4a;
    --ink-soft:#8a8a8a;
    --logo-ink:#3c3c3e;
    --logo-soft:#a9a9ab;
  }
  *{margin:0;padding:0;box-sizing:border-box}
  html,body{width:1200px;height:901px;overflow:hidden}
  body{background:var(--backdrop);display:flex;align-items:center;justify-content:center;gap:50px;font-family:"Open Sans",sans-serif}
  .card{
    position:relative;width:540px;height:310px;border-radius:18px;overflow:hidden;
    background:linear-gradient(var(--band),var(--band-dark));
    box-shadow:0 14px 30px rgba(0,0,0,.45);
  }
  .card__face{
    position:absolute;left:0;right:0;top:56px;bottom:56px;background:var(--paper);
    border-top:7px solid var(--accent);border-bottom:7px solid var(--accent);
    box-shadow:0 -4px 0 #fff, 0 4px 0 #fff;
  }
  .logo-word{
    position:absolute;right:42px;top:22px;
    font-family:"Josefin Sans",sans-serif;font-weight:400;font-size:52px;letter-spacing:2px;color:var(--logo-ink);
  }
  .holder{position:absolute;left:38px;top:88px}
  .holder__name{color:var(--accent);font-weight:600;font-size:17px;line-height:1.1}
  .holder__role{color:var(--ink-soft);font-size:12px;margin-top:2px}
  .holder__rule{position:absolute;left:150px;top:0;width:1px;height:80px;background:#d4d4d4}
  .contacts{position:absolute;left:210px;top:86px;list-style:none;font-size:11.5px;color:var(--ink);line-height:1.45}
  .contacts li{display:flex;align-items:flex-start;gap:8px;margin-bottom:2px}
  .contacts svg{flex:none;margin-top:2px}
  .back-word{
    position:absolute;inset:0;display:flex;flex-direction:column;justify-content:center;padding-left:60px;
    font-family:"Josefin Sans",sans-serif;font-weight:300;font-size:40px;line-height:1.05;letter-spacing:3px;color:var(--logo-soft);
  }
</style>
</head>
<body>
  <article class="card card--front">
    <div class="card__face">
      <div class="logo-word">SOLVIK</div>
      <div class="holder">
        <p class="holder__name">Elin Berg</p>
        <p class="holder__role">Director</p>
        <span class="holder__rule"></span>
      </div>
      <ul class="contacts">
        <li>
          <svg width="10" height="10" viewBox="0 0 10 10"><circle cx="5" cy="5" r="5" fill="var(--accent)"/><path d="M3 2.5l1.5 1.5-0.8 0.8 1.5 1.5 0.8-0.8 1.5 1.5-1 1c-2.5-0.5-4-2-4.5-4.5z" fill="#fff"/></svg>
          <span>48 Linden Park Road<br>Riverton, New York</span>
        </li>
        <li>
          <svg width="10" height="10" viewBox="0 0 10 10"><circle cx="5" cy="5" r="5" fill="var(--accent)"/><path d="M3 2.5l1.5 1.5-0.8 0.8 1.5 1.5 0.8-0.8 1.5 1.5-1 1c-2.5-0.5-4-2-4.5-4.5z" fill="#fff"/></svg>
          <span>03 555 014 276</span>
        </li>
        <li>
          <svg width="10" height="10" viewBox="0 0 10 10"><rect width="10" height="10" rx="2" fill="var(--accent)"/><path d="M2 3h6v4H2z M2 3l3 2.2L8 3" fill="none" stroke="#fff" stroke-width=".8"/></svg>
          <span>firstname.lastname@solvikskola.se</span>
        </li>
        <li>
          <svg width="10" height="10" viewBox="0 0 10 10"><circle cx="5" cy="5" r="5" fill="var(--accent)"/><circle cx="5" cy="5" r="2.6" fill="none" stroke="#fff" stroke-width=".8"/><path d="M2.4 5h5.2" stroke="#fff" stroke-width=".8"/></svg>
          <span>solvikskola.se</span>
        </li>
      </ul>
    </div>
  </article>

  <article class="card card--back">
    <div class="card__face">
      <div class="back-word">SOLVIK<br>GRUNDSKOLA</div>
    </div>
  </article>
</body>
</html>
```